Roofing Company Sales Rep Business Card

Business card for sales rep to canvass and hand out to property owners/managers for free roof inspections and roof replacements.

```html
<!DOCTYPE html>
<html lang="en">
<head>
<meta charset="utf-8">
<title>Summit Ridge Roofing – Business Card</title>
<link rel="stylesheet" href="https://fonts.googleapis.com/css2?family=Open+Sans:wght@400;600;700;800&display=swap">
<style>
  :root {
    --page-bg: #2a2a2e;
    --card-bg: #1f1f23;
    --card-edge: #26262b;
    --emboss: #131315;
    --brand-red: #e11d26;
    --white: #ffffff;
    --soft-white: #e9e9ec;
    --divider: #8a8a90;
  }
  * { box-sizing: border-box; margin: 0; padding: 0; }
  html, body {
    width: 1200px; height: 780px; overflow: hidden;
    background: var(--page-bg);
    font-family: "Open Sans", Arial, sans-serif;
  }
  .canvas {
    position: relative; width: 1200px; height: 780px;
  }
  .card {
    position: absolute; top: 230px;
    width: 560px; height: 320px;
    background: var(--card-bg);
    border-radius: 20px;
    overflow: hidden;
    box-shadow: 0 18px 40px rgba(0,0,0,.45);
  }
  .card--front { left: 25px; }
  .card--back { left: 615px; }
  .card__swoosh {
    position: absolute; inset: 0; width: 100%; height: 100%;
  }
  .swoosh-red { fill: var(--brand-red); }
  .swoosh-white { fill: var(--white); }

  /* Front */
  .front-brand {
    position: absolute; left: 0; right: 0; top: 110px;
    text-align: center;
    font-weight: 800; font-size: 40px; letter-spacing: 1px;
    color: var(--emboss);
    text-transform: uppercase;
  }

  /* Back */
  .back-brand {
    position: absolute; left: 34px; top: 102px; width: 200px;
    font-weight: 800; font-size: 28px; line-height: 1.1;
    color: var(--white); text-transform: uppercase;
  }
  .divider {
    position: absolute; left: 262px; top: 48px;
    width: 1px; height: 150px; background: var(--divider);
  }
  .contact {
    position: absolute; left: 290px; top: 44px; right: 20px;
    color: var(--white);
  }
  .contact__name {
    font-weight: 700; font-size: 27px; line-height: 1.1;
  }
  .contact__first { color: var(--brand-red); }
  .contact__title {
    font-weight: 600; font-size: 15px; margin-top: 2px; color: var(--soft-white);
  }
  .contact__list { list-style: none; margin-top: 16px; }
  .contact__item {
    display: flex; align-items: center; gap: 9px;
    font-size: 14px; line-height: 24px; color: var(--soft-white);
  }
  .contact__icon { width: 14px; height: 14px; flex: none; }
  .contact__icon * { fill: none; stroke: var(--brand-red); stroke-width: 2; stroke-linecap: round; stroke-linejoin: round; }
  .address {
    position: absolute; left: 34px; top: 222px;
    font-size: 14px; font-weight: 400; color: var(--white);
  }
</style>
</head>
<body>
<main class="canvas">

  <section class="card card--front" aria-label="Card front">
    <svg class="card__swoosh" viewBox="0 0 560 320" aria-hidden="true">
      <polygon class="swoosh-red" points="0,320 0,306 300,268 352,268 300,320"/>
      <polygon class="swoosh-white" points="330,298 560,234 560,262 356,320 318,320"/>
    </svg>
    <div class="front-brand">Summit Ridge Roofing</div>
  </section>

  <section class="card card--back" aria-label="Card back">
    <svg class="card__swoosh" viewBox="0 0 560 320" aria-hidden="true">
      <polygon class="swoosh-red" points="0,320 0,306 300,268 352,268 300,320"/>
      <polygon class="swoosh-white" points="330,298 560,234 560,262 356,320 318,320"/>
    </svg>

    <div class="back-brand">Summit Ridge Roofing</div>
    <div class="divider"></div>

    <div class="contact">
      <h1 class="contact__name"><span class="contact__first">Lena</span> Marsh</h1>
      <p class="contact__title">Managing Director</p>
      <ul class="contact__list">
        <li class="contact__item">
          <svg class="contact__icon" viewBox="0 0 16 16"><path d="M3 2l3 0 1 4-2 1a8 8 0 0 0 4 4l1-2 4 1v3c0 1-1 1-1 1A12 12 0 0 1 2 3s0-1 1-1z"/></svg>
          (555) 204-1187
        </li>
        <li class="contact__item">
          <svg class="contact__icon" viewBox="0 0 16 16"><rect x="1.5" y="3.5" width="13" height="9" rx="1"/><path d="M2 4l6 5 6-5"/></svg>
          info@summitridge.com
        </li>
        <li class="contact__item">
          <svg class="contact__icon" viewBox="0 0 16 16"><circle cx="8" cy="8" r="6.5"/><path d="M1.5 8h13M8 1.5c2.5 2.5 2.5 10.5 0 13M8 1.5c-2.5 2.5-2.5 10.5 0 13"/></svg>
          www.summitridge.com
        </li>
      </ul>
    </div>

    <p class="address">1480 Cedar Hollow Rd. Suite 300 Lakemont, TX 75099</p>
  </section>

</main>
</body>
</html>
```